Nolvik Imaging Center web design and code

We need a new website for a Diagnostic Imaging Center in Fort Lauderdale, Florida.
The center has new RO advanced diagnostic equipment including a 3.0 Tesla MRI, a 128 slice PET/CT and a Varen T4 Ultrasound. Our facility has just been renovated and we have a lot of images, both facility and modality to use.
We have two client types, doctors who send their patients to our clinical Nolvik Center division, and clients who self-refer for screening studies to our Wellspire division. Both logos are attached. Please use the colors in the logos for the layout. Site should be coded in conventional HTML with CSS, but support multiple devices.
Updates

Reason: Waiting for additional designs. Most of the current designs are very similar in their structure and we would like more variety in terms of layout.

Target Market(s)

Doctors who refer patients for MRI, CT, PET, Bone Density and Ultrasound scans,
and
Retail clients who want full-body screening using MRI.

Industry/Entity Type

Medical Imaging

Coding

Coded - Design and coding required

Number of Pages Required

5+ page

Font styles to use
Sans Serif
Other font styles liked:
• Arquitecta

Requirements
Must have
• A good balance between color, shape, message and people/machine images.
• Must have images of the various machines, (RO Quillmark TN480, RO Quillmark 370, RO Varen T4) happy patients, clinical people, facility images and information about scans, preparations, costs, insurances we take.
• Must have links for social media and dynamic imagery.
Nice to have
• Some interactivity would be nice, including contact forms and scheduling application, Location map, directions, downloadable forms, history.
Should not have
• We do not want this to be built on WordPress platform. Should not be bound to a database platform that is proprietary or difficult to move.

```html
<!DOCTYPE html>
<html lang="en">
<head>
<meta charset="utf-8">
<title>Nolvik Imaging Center</title>
<link href="https://fonts.googleapis.com/css2?family=Lato:wght@400;700;900&family=Open+Sans:wght@400;600;700&display=swap" rel="stylesheet">
<style>
:root{
  --green:#8dc63f;
  --green-dark:#6fa52a;
  --ink:#333;
  --muted:#666;
  --charcoal:#3b3b3b;
  --grey-band:#555;
  --line:#ddd;
  --white:#fff;
}
*{box-sizing:border-box;margin:0;padding:0}
html,body{width:739px;height:1200px;overflow:hidden;background:var(--white)}
body{font-family:"Open Sans",sans-serif;color:var(--ink);position:relative}
.site-header{height:82px;display:flex;align-items:center;justify-content:space-between;padding:0 28px}
.brand{display:flex;align-items:center;gap:10px}
.brand-mark{width:40px;height:40px;border-radius:50%;background:var(--green)}
.brand-name{font-family:"Lato",sans-serif;font-weight:900;font-size:17px;line-height:19px;color:var(--charcoal);text-transform:uppercase}
.call{display:flex;align-items:center;gap:8px;font-size:12px;color:var(--charcoal)}
.call b{font-weight:700}
.main-nav{height:18px;background:var(--green);display:flex;justify-content:center;gap:26px;align-items:center}
.main-nav a{color:var(--white);font-size:8px;font-weight:700;text-decoration:none;text-transform:uppercase;letter-spacing:.3px}
.main-nav a.active{background:var(--green-dark);padding:5px 8px}
.hero{position:relative;height:238px;margin:0 14px;border-bottom:3px solid var(--green)}
.hero-photo{position:absolute;inset:0;background:linear-gradient(120deg,#e8eef2 0%,#c9d5dd 45%,#8aa6b8 75%,#4f6f86 100%)}
.appointment{position:absolute;right:6px;top:18px;width:226px;height:200px;background:rgba(55,55,55,.92);border-radius:60px 0 0 60px;padding:14px 16px 0 44px}
.appointment h3{font-family:"Lato",sans-serif;font-weight:400;color:var(--white);font-size:15px;text-align:right;line-height:17px}
.appointment h3 span{display:block;color:var(--green);font-weight:900;font-size:18px;text-transform:uppercase}
.field{height:13px;background:var(--white);margin-top:6px;font-size:7px;color:#999;padding:2px 5px}
.field.msg{height:28px}
.submit{display:block;margin:8px 0 0 auto;background:var(--green);color:var(--white);font-size:8px;font-weight:700;padding:4px 10px;width:max-content}
.about{text-align:center;padding:18px 70px 0}
.about h2{font-family:"Lato",sans-serif;font-weight:900;font-size:20px;color:var(--charcoal);text-transform:uppercase}
.about .rule{width:40px;height:2px;background:var(--green);margin:8px auto 16px}
.about p{font-size:8px;line-height:13px;color:var(--muted);margin-bottom:12px}
.services{position:absolute;top:638px;left:0;width:739px;height:256px;background:linear-gradient(180deg,#6a6a6a,#4a4a4a)}
.service{position:absolute;top:48px;width:172px;height:176px;background:var(--white);text-align:center;padding:48px 16px 0}
.service .badge{position:absolute;top:-26px;left:50%;margin-left:-28px;width:56px;height:56px;border-radius:50%;background:var(--green);border:3px solid var(--white);box-shadow:0 0 0 2px var(--green);color:var(--white);font-family:"Lato",sans-serif;font-weight:900;font-size:16px;line-height:50px}
.service p{font-size:8px;line-height:12px;color:var(--muted)}
.service a{display:block;margin-top:10px;font-size:7px;color:var(--green-dark);font-weight:700;text-decoration:none}
.lower{position:absolute;top:912px;left:0;width:739px;display:flex;gap:48px;padding:0 60px}
.conditions{width:200px;margin-top:22px}
.conditions h4{background:var(--green);color:var(--white);font-family:"Lato",sans-serif;font-weight:400;font-size:12px;padding:4px 10px}
.conditions li{list-style:none;display:flex;align-items:center;gap:8px;border:1px solid var(--line);border-top:none;height:17px;font-size:8px;color:var(--ink)}
.conditions li i{width:17px;height:16px;background:var(--charcoal);color:var(--white);font-style:normal;font-size:10px;text-align:center;line-height:16px}
.news{flex:1}
.news h4{font-family:"Lato",sans-serif;font-weight:400;font-size:15px;color:var(--charcoal);border-bottom:1px solid var(--line);padding-bottom:6px}
.tabs{display:flex;gap:6px;margin-top:8px}
.tabs span{font-size:8px;padding:4px 16px;background:var(--green);color:var(--white)}
.tabs span.on{background:var(--charcoal)}
.news-box{border:1px solid var(--line);margin-top:0;padding:10px;display:flex;gap:10px;height:110px}
.news-thumb{width:50px;height:40px;background:linear-gradient(135deg,#cfd8de,#8fa3b1);flex:none}
.news-box p{font-size:7px;line-height:11px;color:var(--muted)}
.site-footer{position:absolute;bottom:0;left:0;width:739px;height:52px;background:var(--green);display:flex;align-items:center;padding:0 28px;justify-content:space-between}
.site-footer .brand-name{color:var(--white)}
.site-footer .brand-mark{background:var(--white)}
.foot-right{text-align:right}
.foot-nav{display:flex;gap:10px;font-size:7px;color:var(--white);text-transform:uppercase}
.social{display:flex;gap:4px;justify-content:center;margin:5px 0}
.social i{width:12px;height:12px;background:var(--charcoal);display:block}
.copy{font-size:6px;color:var(--white);text-align:center}
</style>
</head>
<body>
<header class="site-header">
  <div class="brand"><span class="brand-mark"></span><span class="brand-name">Nolvik<br>Imaging Center</span></div>
  <div class="call">
    <svg width="16" height="16" viewBox="0 0 24 24"><circle cx="12" cy="12" r="12" fill="#3b3b3b"/><path d="M8 6l2 3-1.3 1.3a7 7 0 004 4L14 13l3 2-1 2.5c-5 0-10-5-10-10z" fill="#fff"/></svg>
    <span><b>Call Us :</b> 08 5550 1294</span>
  </div>
</header>
<nav class="main-nav">
  <a class="active" href="#">Home</a><a href="#">Departments</a><a href="#">Doctors</a><a href="#">Services</a><a href="#">News</a><a href="#">Audio</a><a href="#">Gallery</a><a href="#">Contact</a>
</nav>
<section class="hero">
  <div class="hero-photo" role="img" aria-label="Technician preparing a patient for an MRI scan"></div>
  <form class="appointment">
    <h3>Make An <span>Appointment:</span></h3>
    <div class="field">Name</div>
    <div class="field">Email</div>
    <div class="field">Phone</div>
    <div class="field msg">Message</div>
    <span class="submit">SUBMIT</span>
  </form>
</section>
<section class="about">
  <h2>About Nolvik Imaging Center</h2>
  <div class="rule"></div>
  <p>Our imaging center offers advanced diagnostic scans in a calm and modern setting. Our team of skilled technicians and radiologists works with referring doctors to deliver clear results quickly. Each visit is planned around patient comfort, with friendly staff, short waiting times and easy scheduling for every type of scan we provide. We accept most major insurance plans and help patients understand preparation steps before they arrive.</p>
  <p>From full body screening to focused studies, our renovated facility uses the latest equipment to give accurate images with less time on the table. Patients may book online, call our front desk, or ask their doctor to send a referral directly to our clinical team today.</p>
</section>
<section class="services">
  <article class="service" style="left:62px"><span class="badge">MRI</span><p>Detailed magnetic imaging of soft tissue, joints, brain and spine with a quiet open bore and short scan times for patient comfort.</p><a href="#">Read More »</a></article>
  <article class="service" style="left:283px"><span class="badge">CT</span><p>Fast cross section scans of the chest, abdomen and bones with low dose settings and same day reports for referring doctors.</p><a href="#">Read More »</a></article>
  <article class="service" style="left:504px"><span class="badge">PET</span><p>Functional imaging that shows how organs and tissue work, helping doctors plan care and track progress over time.</p><a href="#">Read More »</a></article>
</section>
<section class="lower">
  <div class="conditions">
    <h4>Common Foot condition:</h4>
    <ul>
      <li><i>+</i>Ankle Replacement</li>
      <li><i>+</i>Ankle Trauma</li>
      <li><i>+</i>Tendon Rupture</li>
      <li><i>+</i>Heel Pain</li>
      <li><i>+</i>Sports Medicine Services</li>
    </ul>
  </div>
  <div class="news">
    <h4>Health News</h4>
    <div class="tabs"><span class="on">Recent</span><span>Popular</span></div>
    <div class="news-box">
      <div class="news-thumb" role="img" aria-label="News story thumbnail"></div>
      <p>New screening hours now open on weekends for full body scans. Patients can book a slot online and receive results within two days. Our team also shares simple tips on how to prepare for each scan, what to wear, and what to bring to your visit so the day runs smoothly.</p>
    </div>
  </div>
</section>
<footer class="site-footer">
  <div class="brand"><span class="brand-mark"></span><span class="brand-name">Nolvik<br>Imaging Center</span></div>
  <div class="foot-right">
    <div class="foot-nav"><span>Home</span><span>Departments</span><span>Doctors</span><span>Services</span><span>News</span><span>Audio</span><span>Gallery</span><span>Contact</span></div>
    <div class="social"><i></i><i></i><i></i></div>
    <div class="copy">Copyright © 2015 Nolvik Imaging Center. All rights reserved.</div>
  </div>
</footer>
</body>
</html>
```